Flyer needed to promote gutter clearance service for established gardening company

We need a bright and engaging flyer to be designed to advertise our gutter clearance service.
Whilst we are a gardening company that normally does more horticultural work, during the winter we offer other services such as gutter clearance where we remove the debris from gutters and thereby reducing the risk of clogs, leakage, breakage and potential structural damage to the property.

Full details of our service, together with our overall brand and colours can be seen on www.hartleyoutdoorcare.co.uk/gutters.

We would like you to use the page on the website as a basis to create the flyer and so please feel free to use as much or as little of the wording contained within the webpage on the flyer drawing particular attention to "Prices starting at just £60 for an average 3 bed house". I will upload pictures but please feel free to use other graphics and fonts to make it stand out.

The contact details which should be included within the flyer are as follows:

Hartley Outdoor Care Ltd
Kestrel Trade Park
Whitlow Moor Ind Estate
Swindon
SN3 7QL

Tel: 01793 418203
www.hartleyoutdoorcare.co.uk
mark@hartleyoutdoorcare.co.uk

The flyers will eventually be printed out in A5 (210mm x 148mm) using Printaloft and so needs to be in that size and suitable file for upload.

I have only put this as a 2 day project as its really urgent and I'm hoping we get some great designs in that time.

Target Market(s)

Homeowners between 25 - 65+

Industry/Entity Type

Home Improvement

Font styles to use
Serif
Sans Serif
Decorative
Script

Colors
6b449b
9bcb3c

Requirements
Must have
• Our colours are purple and green as seen on our website www.hartleyoutdoorcare.co.uk/gutters. Please use those colours.
• The flyer should draw attention to the following facts:
• We are Hartley Outdoor Care Ltd (see attached logo)
• We are offering a Gutter Clearance Service in Swindon
• Prices start at just £60 for the average 3 bed house.
• We are fully insured.
• Our contact details must be included (as in the product description above)
• I have attached pictures but feel free to add other graphics or use fonts to make the flyer more engaging and interesting.
• Additional wording may be taken from the website at the address shown above. You can use as much or as little wording as you like just as long as the message gets across and the flyer contains our contact information and logo and the details shown above.
Nice to have
• I would like a bright and modern design which isn't too busy or cluttered. It should be something that is quick and easy to read.
Should not have
• I don't want it to look too busy or crowded with small type which people just won't read. Whilst I've said you can take whatever wording you want from our website, I'd suggest you don't take it all or too much. I want the main message (as detailed above in 'must haves') to stand out rather than have it contained deep within lots of small type face.

```html
<!DOCTYPE html>
<html lang="en">
<head>
<meta charset="utf-8">
<title>Hartley Outdoor Care – Gutter Clearance Flyer</title>
<link rel="stylesheet" href="https://fonts.googleapis.com/css2?family=Bebas+Neue&family=Oswald:wght@400;500&display=swap">
<style>
  :root {
    --page-bg: #e4e4e4;
    --paper: #ffffff;
    --brand-purple: #6b449b;
    --brand-purple-light: #8a62bb;
    --brand-green: #9bcb3c;
    --lime-soft: #dfe6a0;
    --lime-deep: #c3cf5e;
    --pale-green: #eef3d2;
    --ink: #2e2a24;
    --ink-soft: #5a554c;
    --logo-brown: #3b2a1e;
  }
  * { box-sizing: border-box; margin: 0; padding: 0; }
  html, body {
    width: 1200px; height: 700px; overflow: hidden;
    background: radial-gradient(ellipse at 50% 40%, #efefef 0%, var(--page-bg) 70%, #d4d4d4 100%);
    font-family: "Oswald", "Arial Narrow", sans-serif;
  }
  .flyer {
    position: absolute; left: 374px; top: 30px;
    width: 452px; height: 640px;
    background: var(--paper);
    box-shadow: 0 10px 30px rgba(0,0,0,.22);
    overflow: hidden;
  }
  .photo { position: absolute; }
  .photo--ladder { left: 0; top: 0; width: 116px; height: 112px;
    background: linear-gradient(160deg, #8d6b4a, #c26a3a 45%, #6a5a45); }
  .photo--leaves { left: 121px; top: 0; width: 331px; height: 112px;
    background: linear-gradient(110deg, #3e3f44 0%, #6a6b70 35%, #c59a3c 60%, #6f8d3a 85%, #4d6d2a 100%); }
  .photo--moss { left: 290px; top: 118px; width: 162px; height: 168px;
    background: linear-gradient(180deg, #cfd3d6 0%, #7a6a4e 40%, #5d6d35 70%, #8c8c88 100%); }
  .photo--before { left: 0; top: 366px; width: 168px; height: 168px;
    background: linear-gradient(180deg, #6b5a44 0%, #a88f5a 40%, #7b6a4c 75%, #5e7c3a 100%); }
  .photo--after { left: 174px; top: 366px; width: 278px; height: 168px;
    background: linear-gradient(90deg, #6d6151 0%, #9a958a 35%, #b8b4aa 55%, #5c8a35 80%, #4d7a2d 100%); }

  .pale-band { position: absolute; left: 0; top: 112px; width: 452px; height: 8px; background: var(--pale-green); }

  .intro {
    position: absolute; left: 0; top: 118px; width: 286px; height: 160px;
    background: linear-gradient(135deg, var(--lime-soft) 0%, #d6df7f 50%, var(--lime-deep) 100%);
    padding: 22px 16px 0 22px;
  }
  .intro__text {
    font-size: 9.6px; line-height: 1.45; letter-spacing: .3px;
    text-transform: uppercase; text-align: justify; color: var(--ink);
  }

  .price-banner {
    position: absolute; left: 0; top: 280px; width: 452px; height: 52px;
    background: linear-gradient(90deg, var(--brand-purple) 0%, var(--brand-purple-light) 100%);
    color: #fff; text-align: center;
    font-size: 18px; font-weight: 500; line-height: 1.05; padding-top: 7px;
  }

  .compare-labels { position: absolute; left: 0; top: 332px; width: 452px; height: 34px;
    background: linear-gradient(90deg, #fff 0%, #f4f1f7 100%); }
  .compare-labels__before, .compare-labels__after {
    position: absolute; font-family: "Bebas Neue", "Oswald", sans-serif;
    font-size: 22px; letter-spacing: 9px; line-height: 1;
  }
  .compare-labels__before { left: 6px; top: 2px; color: var(--brand-green); }
  .compare-labels__after { right: 0; top: 12px; color: var(--brand-purple); }

  .footer { position: absolute; left: 0; top: 534px; width: 452px; height: 106px;
    background: linear-gradient(180deg, #f2f2f2, #fff); }
  .footer__address, .footer__contact {
    position: absolute; top: 12px; font-size: 8.4px; line-height: 1.25;
    text-transform: uppercase; color: var(--ink-soft); letter-spacing: .2px;
  }
  .footer__address { left: 8px; }
  .footer__contact { left: 118px; }

  .brand { position: absolute; right: 22px; bottom: 18px; display: flex; align-items: center; gap: 7px; }
  .brand__dot { width: 16px; height: 16px; border-radius: 50%; background: var(--brand-green); }
  .brand__name { font-size: 17px; font-weight: 500; color: var(--logo-brown); line-height: 1; }
</style>
</head>
<body>
  <main class="flyer">
    <div class="photo photo--ladder" role="img" aria-label="Worker on a ladder clearing a gutter"></div>
    <div class="photo photo--leaves" role="img" aria-label="Gloved hand removing autumn leaves from a roof gutter"></div>
    <div class="pale-band"></div>

    <section class="intro">
      <p class="intro__text">Clearing gutters is not just a dirty job but it can be a dangerous one too if not done properly. At Hartley Outdoor Care, we are fully insured and use the latest tools and techniques to safely clear your gutters, giving you peace of mind without having to risk getting dirty or injured yourself.</p>
    </section>
    <div class="photo photo--moss" role="img" aria-label="Moss and debris being lifted out of a gutter"></div>

    <section class="price-banner">with prices starting at just £60 to clear the<br>gutters of an average 3 bed house!</section>

    <div class="compare-labels">
      <span class="compare-labels__before">Before</span>
      <span class="compare-labels__after">After</span>
    </div>
    <div class="photo photo--before" role="img" aria-label="Gutter clogged with leaves before clearing"></div>
    <div class="photo photo--after" role="img" aria-label="Clean empty gutter after clearing"></div>

    <footer class="footer">
      <address class="footer__address" style="font-style:normal">
        Hartley Outdoor Care Ltd<br>Kestrel Trade Park<br>Whitlow Moor Ind Estate<br>Swindon<br>SN3 7QL
      </address>
      <div class="footer__contact">
        Tel: 01793 418203<br>www.hartleyoutdoorcare.co.uk<br>mark@hartleyoutdoorcare.co.uk
      </div>
      <div class="brand">
        <span class="brand__dot"></span>
        <span class="brand__name">Hartley Outdoor Care</span>
      </div>
    </footer>
  </main>
</body>
</html>
```